New Business Card Design Project

Use the flyer uploaded and website www.brightoakbuilders.com for inspiration.
List Our Services on Backside of business cards
Martin Hollis
Harborline Renovations Inc.
Licensed General Contractors
858-471-9063

Contact Information for Business Card

Use the flyer uploaded and website www.brightoakbuilders.com for inspiration. List Our Services on Backside of business cards Martin Hollis Harborline Renovations Inc. Licensed General Contractors 858-471-9063

```html
<!DOCTYPE html>
<html lang="en">
<head>
<meta charset="utf-8">
<title>Harborline Renovations – Business Card</title>
<link href="https://fonts.googleapis.com/css2?family=Oswald:wght@300;400;600;700&display=swap" rel="stylesheet">
<style>
  :root{
    --bg:#acacac;
    --ink:#111111;
    --paper:#ffffff;
    --red:#e8141c;
    --blue:#3483c8;
    --fern:#5c9b2c;
    --fern-light:#8cc04a;
    --muted:#666666;
    --emboss:#2b2b2b;
  }
  *{margin:0;padding:0;box-sizing:border-box}
  html,body{width:1200px;height:1000px;overflow:hidden}
  body{background:var(--bg);font-family:'Oswald',sans-serif;position:relative}
  .card{position:absolute;left:294px;width:613px;height:352px;overflow:hidden;box-shadow:0 18px 40px rgba(0,0,0,.35)}
  .card--front{top:117px;background:var(--paper)}
  .card--back{top:536px;background:var(--ink)}
  .front-art{position:absolute;inset:0}
  .brand{position:absolute;left:20px;top:86px;width:160px;text-align:center;color:var(--paper);font-weight:400;font-size:12.5px;letter-spacing:.6px;line-height:16px;white-space:nowrap}
  .headline{position:absolute;right:30px;top:70px;text-align:right;color:var(--red);font-weight:600;font-size:23px;line-height:25px;letter-spacing:.3px}
  .services{position:absolute;right:30px;top:132px;list-style:none;text-align:right}
  .services li{font-size:18px;line-height:25px;letter-spacing:-.2px;color:var(--ink);display:flex;justify-content:flex-end;align-items:center;gap:8px;white-space:nowrap}
  .services svg{width:17px;height:17px;flex:none}
  .contact{position:absolute;left:51px;top:218px}
  .contact__name{color:var(--red);font-weight:600;font-size:28px;line-height:34px}
  .contact__role{color:var(--muted);font-weight:300;font-size:14px;line-height:16px}
  .contact__rule{width:79px;height:2px;background:var(--red);margin:8px 0 7px}
  .contact__phone{display:flex;align-items:center;gap:4px;font-weight:600;font-size:19px;line-height:24px;color:var(--ink)}
  .contact__web{font-size:19px;line-height:24px;color:var(--ink)}
  .back-brand{position:absolute;left:0;right:0;top:212px;text-align:center;color:var(--emboss);font-size:36px;line-height:44px;letter-spacing:3px;font-weight:400;white-space:nowrap}
</style>
</head>
<body>
  <section class="card card--front">
    <svg class="front-art" width="613" height="352" viewBox="0 0 613 352">
      <defs>
        <radialGradient id="frondTop" cx="0.6" cy="0.4" r="0.6">
          <stop offset="0" stop-color="var(--fern)" stop-opacity=".9"/>
          <stop offset=".6" stop-color="var(--fern-light)" stop-opacity=".55"/>
          <stop offset="1" stop-color="var(--fern-light)" stop-opacity="0"/>
        </radialGradient>
        <radialGradient id="frondLeft" cx="0.35" cy="0.5" r="0.6">
          <stop offset="0" stop-color="var(--fern)" stop-opacity=".9"/>
          <stop offset=".6" stop-color="var(--fern-light)" stop-opacity=".55"/>
          <stop offset="1" stop-color="var(--fern-light)" stop-opacity="0"/>
        </radialGradient>
      </defs>
      <polygon points="0,0 613,0 613,8 0,192" fill="var(--ink)"/>
      <rect x="520" y="0" width="93" height="150" fill="url(#frondTop)" role="img" aria-label="Palm frond illustration, top right corner"/>
      <rect x="0" y="140" width="90" height="135" fill="url(#frondLeft)" role="img" aria-label="Palm frond illustration, left edge"/>
      <polyline points="13,352 13,175 597,3 597,352" fill="none" stroke="var(--blue)" stroke-width="4"/>
    </svg>

    <div class="brand">HARBORLINE RENOVATIONS</div>

    <h2 class="headline">OUR SERVICES ARE<br>100% GUARANTEED</h2>

    <ul class="services">
      <li>Remodel: Kitchen &amp; Bath <svg viewBox="0 0 20 20"><circle cx="10" cy="10" r="7.5" fill="none" stroke="var(--red)" stroke-width="2"/><path d="M6,10 l3,3 l8,-9" fill="none" stroke="var(--red)" stroke-width="2"/></svg></li>
      <li>Painting: Interior &amp; Exterior <svg viewBox="0 0 20 20"><circle cx="10" cy="10" r="7.5" fill="none" stroke="var(--red)" stroke-width="2"/><path d="M6,10 l3,3 l8,-9" fill="none" stroke="var(--red)" stroke-width="2"/></svg></li>
      <li>Flooring: Carpet, Vinyl, Wood <svg viewBox="0 0 20 20"><circle cx="10" cy="10" r="7.5" fill="none" stroke="var(--red)" stroke-width="2"/><path d="M6,10 l3,3 l8,-9" fill="none" stroke="var(--red)" stroke-width="2"/></svg></li>
      <li>Window &amp; Door Replacement <svg viewBox="0 0 20 20"><circle cx="10" cy="10" r="7.5" fill="none" stroke="var(--red)" stroke-width="2"/><path d="M6,10 l3,3 l8,-9" fill="none" stroke="var(--red)" stroke-width="2"/></svg></li>
      <li>Plumbing: Repairs &amp; Upgrades <svg viewBox="0 0 20 20"><circle cx="10" cy="10" r="7.5" fill="none" stroke="var(--red)" stroke-width="2"/><path d="M6,10 l3,3 l8,-9" fill="none" stroke="var(--red)" stroke-width="2"/></svg></li>
      <li>Deck &amp; Patio Construction <svg viewBox="0 0 20 20"><circle cx="10" cy="10" r="7.5" fill="none" stroke="var(--red)" stroke-width="2"/><path d="M6,10 l3,3 l8,-9" fill="none" stroke="var(--red)" stroke-width="2"/></svg></li>
      <li>Water &amp; Mold Damage <svg viewBox="0 0 20 20"><circle cx="10" cy="10" r="7.5" fill="none" stroke="var(--red)" stroke-width="2"/><path d="M6,10 l3,3 l8,-9" fill="none" stroke="var(--red)" stroke-width="2"/></svg></li>
      <li>Garage Renovation <svg viewBox="0 0 20 20"><circle cx="10" cy="10" r="7.5" fill="none" stroke="var(--red)" stroke-width="2"/><path d="M6,10 l3,3 l8,-9" fill="none" stroke="var(--red)" stroke-width="2"/></svg></li>
    </ul>

    <div class="contact">
      <div class="contact__name">Martin Hollis</div>
      <div class="contact__role">Licensed General Contractors</div>
      <div class="contact__rule"></div>
      <div class="contact__phone">
        <svg width="17" height="17" viewBox="0 0 20 20"><circle cx="10" cy="10" r="10" fill="var(--red)"/><path d="M6.5,5 l2,0 l1,3 l-1.3,1 c.8,1.6 1.8,2.6 3.3,3.3 l1,-1.3 l3,1 l0,2 c-5,.5 -9.5,-4 -9,-9z" fill="var(--paper)"/></svg>
        858-471-9063
      </div>
      <div class="contact__web">BrightOakBuilders.com</div>
    </div>
  </section>

  <section class="card card--back">
    <div class="back-brand">HARBORLINE RENOVATIONS</div>
  </section>
</body>
</html>
```